Flyer-Design für verschiedene Anwendungsfälle bzw. Produkte
Zielgruppe
Wir lösen reale Probleme mit digitalen Technologien wie IoT und KI. In unseren Projekten liefern wir Gesamtlösungen von der Strategieberatung über Konzepterstellung bis zur technischen Umsetzung und dem Betrieb. Integration und Konzeption spielen eine große Rolle, wir sind kein Hardwareanbieter, sondern bauen Komplettlösungen aus Software, Connectivity und Hardware. Unsere Kunden sind gehobener Mittelstand bis Konzern, ab 25 Mio € aufwärts. Oft sind unsere Kunden aus konservativen Branchen. Wir müssen beim Design immer einen Kompromiss aus innovativ und Vertrauen erweckend finden. Unsere Persona ist weiß, männlich, über 50, nicht besonders technologieaffin.
Aufgabenstellung
Wir brauchen eine Flyer-Vorlage für verschiedene Anwendungsfälle bzw. Produkte. Im Anhang sind Beispiele für Produktbeschreibungen, sowie ein Flyer, den wir selbst designet haben.
Ergebnis soll ein Flyer-Design sein, das wir für solche Produkte immer wieder verwenden können, DIN A5 zweiseitig.
Exo2 und Trebuchet sind unsere Schriftarten. Logos habe ich in 2 Formaten angehängt.
Website: tavolu.me
Wenn Sie weitere Ideen haben, sind wir ganz Ohr.
Grafisch bitte nur die Farben grau, schwarz und orange verwenden (grau und orange siehe Logo)

```html
<!DOCTYPE html>
<html lang="de">
<head>
<meta charset="utf-8">
<title>TAVOLU Flyer – Vorder- und Rückseite</title>
<link href="https://fonts.googleapis.com/css2?family=Exo+2:wght@500;600;700&family=Open+Sans:wght@400;600&display=swap" rel="stylesheet">
<style>
:root{
  --orange:#ef7d00;
  --slate:#33414f;
  --ink:#3b3b3b;
  --muted:#6a6a6a;
  --panel:#f1f1f1;
  --white:#ffffff;
  --stage:#e4e4e4;
}
*{box-sizing:border-box;margin:0;padding:0}
html,body{width:1200px;height:2702px;overflow:hidden;background:var(--stage)}
body{font-family:"Open Sans",sans-serif;color:var(--ink);position:relative}
.flyer{position:absolute;left:150px;width:900px;height:1273px;background:var(--white);overflow:hidden;box-shadow:0 6px 24px rgba(0,0,0,.12)}
.flyer--front{top:40px}
.flyer--back{top:1389px}

.brand{position:absolute;left:40px;top:52px;display:flex;align-items:center;gap:10px;font-family:"Exo 2",sans-serif;font-weight:700;font-size:34px;letter-spacing:3px;color:var(--orange)}
.brand__dot{width:12px;height:12px;border-radius:50%;background:var(--orange)}
.headline{position:absolute;right:40px;top:40px;text-align:right;font-family:"Exo 2",sans-serif;width:520px}
.headline__kicker{font-weight:700;font-size:17px;color:var(--slate)}
.headline__title{font-weight:700;font-size:30px;line-height:1.1;color:var(--orange);margin-top:4px}

.panel{position:absolute;left:40px;width:820px;background:var(--panel);padding:16px 22px 14px}
.tab{display:inline-block;font-family:"Exo 2",sans-serif;font-weight:700;font-size:17px;color:var(--white);padding:6px 34px 6px 18px;margin:-30px 0 10px -22px;clip-path:polygon(0 0,100% 0,calc(100% - 16px) 100%,0 100%)}
.tab--dark{background:var(--slate)}
.tab--orange{background:var(--orange)}
.case{position:absolute;left:40px;font-family:"Exo 2",sans-serif;font-weight:700;font-size:17px;color:var(--orange)}

.checks{list-style:none}
.checks li{position:relative;padding-left:26px;font-size:14px;line-height:1.45;margin-bottom:4px}
.checks li::before{content:"";position:absolute;left:0;top:4px;width:12px;height:12px;border:1.5px solid currentColor;border-radius:2px}
.checks li::after{content:"";position:absolute;left:4px;top:5px;width:4px;height:8px;border:solid currentColor;border-width:0 2px 2px 0;transform:rotate(45deg)}
.panel .checks li::before,.panel .checks li::after{color:var(--orange)}

.band{position:absolute;left:0;right:0}
.band--orange{background:var(--orange);clip-path:polygon(0 80px,100% 0,100% 100%,0 100%)}
.band--slate{background:var(--slate);clip-path:polygon(0 70px,100% 0,100% 100%,0 100%)}
.band--foot{background:var(--white);clip-path:polygon(0 40px,100% 0,100% 100%,0 100%)}

.block{position:absolute;color:var(--white);z-index:2}
.block__title{font-family:"Exo 2",sans-serif;font-weight:700;font-size:21px;margin-bottom:10px}
.block .checks li{font-size:14.5px}
.block p{font-size:15px;line-height:1.5}

.photo{position:absolute;border-radius:50%;border:6px solid var(--white);background:radial-gradient(circle at 45% 40%,#dfe3e7,#9aa3ab 60%,#5c646b);z-index:3}
.device{position:absolute;z-index:3}
.device__screen{width:100%;height:150px;border:8px solid #1d1d1d;border-radius:6px 6px 0 0;background:linear-gradient(120deg,#f4f4f4 0 45%,#cfd8c8 45% 100%)}
.device__base{height:10px;margin:0 -14px;background:#bdbdbd;border-radius:0 0 8px 8px}
.products{position:absolute;z-index:3;border-radius:14px;background:linear-gradient(135deg,#5a5a5a,#1f1f1f 60%,#3a3a3a)}

.contacts{position:absolute;left:0;right:0;bottom:26px;display:flex;justify-content:space-around;z-index:3;font-size:14px;color:var(--ink)}
.contact{display:flex;align-items:center;gap:10px}
.contact__icon{width:24px;height:24px;background:var(--orange);border-radius:3px;display:flex;align-items:center;justify-content:center}
</style>
</head>
<body>

<section class="flyer flyer--front">
  <div class="brand"><span>TAVOLU</span><span class="brand__dot"></span></div>
  <header class="headline">
    <div class="headline__kicker">LoRaWAN oder NB-IoT:</div>
    <div class="headline__title">Funktion des Aufzugs<br>überwachen</div>
  </header>

  <div class="panel" style="top:170px;height:180px">
    <span class="tab tab--dark">Nutzen und Vorteile</span>
    <ul class="checks">
      <li>Präzise und sofortige Warnung, wenn ein Ort, z.B. eine Straße oder Schiene, von Eis- oder Schneeglätte betroffen ist</li>
      <li>Schnelle Reaktion durch Winterdienst führt zur Vermeidung von Unfällen, Verspätungen und Problemen</li>
      <li>Gerade an Unfallschwerpunkten oder gefährlichen Kurven und Steigungen kann eine frühzeitige Warnung und Winterdienst zu einer deutlichen Steigerung der Sicherheit führen</li>
    </ul>
  </div>

  <div class="panel" style="top:385px;height:170px">
    <span class="tab tab--orange">Funktionsweise</span>
    <ul class="checks">
      <li>Ein Sensor erhebt kontinuierlich alle Informationen, die nötig sind um festzustellen, ob ein Punkt (Straße, Schiene, Landebahn etc.) von Eis- oder Schneeglätte betroffen ist</li>
      <li>Die Daten werden über LoRaWAN oder NB IoT übertragen</li>
      <li>Bei Gefahr wird eine Meldung an die relevanten Personen oder Leitsysteme geschickt</li>
      <li>Die Daten können kontinuierlich beobachtet und ausgewertet werden</li>
    </ul>
  </div>

  <div class="band band--orange" style="top:560px;height:460px"></div>
  <div class="photo" role="img" aria-label="Foto eines Straßensensors an einem Mast" style="left:640px;top:500px;width:200px;height:200px"></div>

  <div class="block" style="top:650px;left:40px;width:560px">
    <div class="block__title">A) Hardware</div>
    <ul class="checks">
      <li>Berührungsloser Straßensensor mit LoRaWAN oder NB IoT Übertragungsmodul wird an kritischen Punkten installiert</li>
      <li>Messparameter: Fahrbahnzustand (trocken, feucht, nass, eisbedeckt, schneebedeckt, Wasser + Eis, chemisch nass), Fahrbahnoberflächentemperatur, Wasserfilmhöhe bis zu 6mm, Taupunkttemperatur, relative Feuchte, Eisanteil in %, Reibung (kalkuliert)</li>
      <li>Messtechnologie: Optische LED Transmitter, Fotodetektoren, Pyrometer, Infrarot</li>
      <li>Kombination mit Wetterstation möglich für bessere und frühere Voraussagen</li>
    </ul>
  </div>

  <div class="band band--slate" style="top:940px;height:300px"></div>
  <div class="device" role="img" aria-label="Laptop mit Dashboard zur Glättewarnung und Karte" style="left:610px;top:890px;width:240px">
    <div class="device__screen"></div>
    <div class="device__base"></div>
  </div>

  <div class="block" style="top:1030px;left:40px;width:540px">
    <div class="block__title">B) Frontend und Benachrichtigungen</div>
    <p>Die Beobachtungen der Sensoren werden in einem Dashboard geographisch und als Heatmap angezeigt. Bei Über- oder Unterschreitung bestimmter Werte werden per Mail oder SMS Meldungen verschickt. Anbindung an Leitsysteme ist ebenfalls möglich.</p>
  </div>

  <div class="band band--foot" style="top:1195px;height:78px"></div>
  <div class="contacts">
    <div class="contact"><span class="contact__icon"><svg width="14" height="14" viewBox="0 0 24 24"><path fill="#fff" d="M6.6 10.8a15 15 0 006.6 6.6l2.2-2.2a1 1 0 011-.25 11.4 11.4 0 003.6.6 1 1 0 011 1V20a1 1 0 01-1 1A17 17 0 013 4a1 1 0 011-1h3.5a1 1 0 011 1c0 1.25.2 2.45.6 3.6a1 1 0 01-.25 1z"/></svg></span>+49(0)1719204583</div>
    <div class="contact"><span class="contact__icon"><svg width="14" height="14" viewBox="0 0 24 24"><path fill="none" stroke="#fff" stroke-width="2" d="M3 6h18v12H3zM3 6l9 7 9-7"/></svg></span>iot@tavolu.me</div>
    <div class="contact"><span class="contact__icon"><svg width="14" height="14" viewBox="0 0 24 24"><g fill="none" stroke="#fff" stroke-width="2"><circle cx="12" cy="12" r="9"/><path d="M3 12h18M12 3c3 3 3 15 0 18M12 3c-3 3-3 15 0 18"/></g></svg></span>www.tavolu.me</div>
  </div>
</section>

<section class="flyer flyer--back">
  <div class="brand"><span>TAVOLU</span><span class="brand__dot"></span></div>
  <header class="headline">
    <div class="headline__kicker">LoRaWAN oder NB-IoT:</div>
    <div class="headline__title">Füllstandsüberwachung und Routenoptimierung Abfallwirtschaft</div>
  </header>

  <div class="case" style="top:160px">Fall 1: große öffentliche Container, z.B. Altglas, Altkleider, Altpapier</div>
  <div class="panel" style="top:215px;height:150px">
    <span class="tab tab--dark">Nutzen und Vorteile</span>
    <ul class="checks">
      <li>Bürger wissen, zu welchen Containern sie ihren Abfall bringen können</li>
      <li>Entsorger kann optimiert leeren und Kosten sparen</li>
      <li>Containerstandorte können datengestützt erweitert oder reduziert werden</li>
      <li>Weniger wilder Müll</li>
    </ul>
  </div>

  <div class="case" style="top:385px">Fall 2: Kleinere städtische Mülleimer, z.B. in Erholungsgebieten</div>
  <div class="panel" style="top:440px;height:140px">
    <span class="tab tab--dark">Nutzen und Vorteile</span>
    <ul class="checks">
      <li>Nutzung der Mülleimer ist stark von unregelmäßigen Faktoren wie Wetter oder Veranstaltungen abhängig</li>
      <li>Starr regelmäßige Leerung führt häufig zu Überfüllung und dadurch Umweltverschmutzung, die durch die Anwendung von Sensoren vermieden wird</li>
      <li>Überflüssige Leerungen werden vermieden und dadurch Kosten gespart</li>
    </ul>
  </div>

  <div class="panel" style="top:615px;height:215px">
    <span class="tab tab--orange">Funktionsweise</span>
    <ul class="checks">
      <li>Im Container werden Sensoren zur Füllstandsmessung angebracht.</li>
      <li>Der Füllstand wird an eine Bürger-Website/-App gemeldet, die nur „voll“, „fast voll“ und „nicht voll“ anzeigt, sowie bei voll oder fast voll eine möglichst nahe gelegene Alternative</li>
      <li>Der Füllstand wird an den Entsorger gemeldet. Hier kann entweder eine Routenoptimierungs-App zur Verfügung gestellt oder die Daten in ein bestehendes Betriebsführungssystem integriert werden.</li>
      <li>Die Daten werden analysiert, um die regelmäßige Auslastung der Container zu bestimmen und ihre Standorte langfristig zu optimieren</li>
    </ul>
  </div>

  <div class="band band--orange" style="top:800px;height:260px"></div>
  <div class="products" role="img" aria-label="Produktfoto verschiedener Füllstandssensoren" style="left:620px;top:830px;width:220px;height:110px"></div>

  <div class="block" style="top:900px;left:40px;width:520px">
    <div class="block__title">A) Hardware</div>
    <p>Ultraschall-, Radar- oder optische Sensoren messen den Abstand zwischen sich selbst und der Oberfläche und erkennen so den Füllstand</p>
  </div>

  <div class="band band--slate" style="top:1010px;height:263px"></div>
  <div class="block" style="top:1100px;left:40px;width:820px">
    <div class="block__title">B) Frontend und Benachrichtigungen</div>
    <ul class="checks">
      <li>Darstellung in einer Web App (für Mobilgeräte und PCs) auf einer Karte für Bürger, mit Anzeige von Alternativen bei vollen Containern</li>
      <li>Einbindung in Routenoptimierungs- oder Betriebsführungs-Anwendung beim Entsorger</li>
      <li>Alarmierung bei Überschreitung von Grenzwerten möglich</li>
    </ul>
  </div>
</section>

</body>
</html>
```